Catalog for our Gold Coins for high value market

We need someone who makes our catalog or book for the gold coins of Switzerland.
Please use the Word Document. The text and the images are below. Feel free to make a nice design. Also make a nice design as a title.
Please use Adobe Indesign or Illustrator to make the content adjustable for us if needed.

You could also add a "star rating" from 1-4 for some of the coins with an image. I will do the rating later. It should be a rating of how precious the coins are without entering a price.
You could also adjust the title design with the coins.

Please make at least the following pages:
Title
Table of content
Title Page for each Ares (Aargau Page 6, Appenzell Page 6, Basel Page 8 and so on)
Pages with the content (Coins including the description)

Target Market(s)

Gold coins collectors. Usually those people are rich men.

Requirements
Must have
• Modern design
Should not have
• Not too many colors used. It should be modern. But have some class.

```html
<!DOCTYPE html>
<html lang="de">
<head>
<meta charset="UTF-8">
<title>Goldmünzen der Kantone und Eidgenossenschaft – Titel</title>
<link href="https://fonts.googleapis.com/css2?family=Josefin+Sans:wght@600;700&display=swap" rel="stylesheet">
<style>
  :root {
    --blue-deep: #1a1f86;
    --blue-mid: #2a36b4;
    --blue-light: #3b4cc8;
    --gold: #c9a043;
    --gold-light: #e8d48e;
    --gold-pale: #f3e6b0;
    --white: #ffffff;
  }
  html, body {
    margin: 0;
    padding: 0;
    width: 848px;
    height: 1200px;
    overflow: hidden;
    background: var(--blue-deep);
  }
  .cover {
    position: relative;
    width: 848px;
    height: 1200px;
    overflow: hidden;
    background:
      radial-gradient(ellipse 70% 45% at 50% 35%, var(--blue-light) 0%, var(--blue-mid) 45%, var(--blue-deep) 100%);
    font-family: "Josefin Sans", sans-serif;
    color: var(--white);
  }
  .cover__rings {
    position: absolute;
    inset: 0;
  }
  .brand {
    position: absolute;
    top: 148px;
    left: 0;
    width: 100%;
    display: flex;
    justify-content: center;
    align-items: center;
    gap: 14px;
  }
  .brand__mark {
    width: 22px;
    height: 22px;
    background: var(--white);
  }
  .brand__name {
    font-weight: 700;
    font-size: 40px;
    letter-spacing: 2px;
    text-transform: uppercase;
    color: var(--white);
  }
  .title__label {
    position: absolute;
    left: 190px;
    top: 459px;
    width: 458px;
    height: 87px;
    background: linear-gradient(90deg, var(--gold) 0%, #d4ae55 55%, rgba(201,160,67,0) 100%);
    display: flex;
    align-items: center;
  }
  .title__label span {
    padding-left: 36px;
    padding-top: 6px;
    font-weight: 600;
    font-size: 50px;
    letter-spacing: 3px;
  }
  .title__sub {
    position: absolute;
    top: 574px;
    left: 0;
    width: 100%;
    margin: 0;
    text-align: center;
    font-weight: 600;
    font-size: 48px;
    line-height: 64px;
    letter-spacing: 3px;
  }
  .cover__photo {
    position: absolute;
    left: 0;
    top: 740px;
    width: 848px;
    height: 420px;
    background:
      radial-gradient(ellipse 40% 45% at 48% 60%, rgba(220,205,170,0.55), rgba(0,0,0,0) 70%),
      linear-gradient(180deg, rgba(26,31,134,0) 0%, rgba(40,40,110,0.6) 35%, rgba(120,105,90,0.7) 65%, rgba(232,212,142,0.9) 100%);
  }
  .cover__swoosh {
    position: absolute;
    inset: 0;
  }
  .cover__band {
    position: absolute;
    left: 0;
    bottom: 0;
    width: 848px;
    height: 60px;
    background: linear-gradient(90deg, var(--gold) 0%, var(--gold-light) 50%, var(--gold-pale) 100%);
  }
</style>
</head>
<body>
<main class="cover">
  <svg class="cover__rings" width="848" height="1200" viewBox="0 0 848 1200" aria-hidden="true">
    <circle cx="430" cy="560" r="320" fill="none" stroke="rgba(255,255,255,0.05)" stroke-width="40"/>
    <circle cx="430" cy="560" r="220" fill="none" stroke="rgba(255,255,255,0.04)" stroke-width="30"/>
    <circle cx="430" cy="560" r="120" fill="none" stroke="rgba(255,255,255,0.04)" stroke-width="20"/>
  </svg>

  <header class="brand">
    <span class="brand__mark"></span>
    <span class="brand__name">Münzhaus Berger</span>
  </header>

  <div class="title__label"><span>GOLDMÜNZEN</span></div>
  <h1 class="title__sub">DER KANTONE UND<br>EIDGENOSSENSCHAFT</h1>

  <div class="cover__photo" role="img" aria-label="Hand in Handschuh nimmt eine Münze aus einer Sammelbox mit Goldmünzen"></div>

  <svg class="cover__swoosh" width="848" height="1200" viewBox="0 0 848 1200" aria-hidden="true">
    <defs>
      <linearGradient id="goldSweep" x1="0" y1="0" x2="1" y2="0">
        <stop offset="0" stop-color="#c9a043"/>
        <stop offset="0.5" stop-color="#f3e6b0"/>
        <stop offset="1" stop-color="#e8d48e"/>
      </linearGradient>
    </defs>
    <path d="M0 1010 Q300 1150 848 1040 L848 1060 Q300 1170 0 1030 Z" fill="url(#goldSweep)" opacity="0.55"/>
    <path d="M0 1070 Q420 1200 848 1090 L848 1140 L0 1140 Z" fill="url(#goldSweep)" opacity="0.45"/>
    <path d="M40 940 Q200 1080 560 1100" fill="none" stroke="#f3e6b0" stroke-width="3" opacity="0.6"/>
  </svg>

  <div class="cover__band"></div>
</main>
</body>
</html>
```